Buss cards
Stationary & envelops
Buss cards - Transportation
Creative Brief
Simple
Harbor Crest Moving
412 West 57th Avenue Brooklyn, NY 11204
Info@Harborcrestmoving.example
www.harborcrestmoving.example
US DOT # 4718392
this is a moving company, that relocates household goods, any ideas you may have would be appreciated
Local & Long Distance Residential & Commercial Storage Facility visit us online: www.harborcrestmoving.example

```html
<!DOCTYPE html>
<html lang="en">
<head>
<meta charset="utf-8">
<title>Harbor Crest Moving – Business Cards</title>
<link href="https://fonts.googleapis.com/css2?family=Open+Sans:wght@400;600;800&display=swap" rel="stylesheet">
<style>
  :root {
    --backdrop: #ecebe8;
    --card: #ffffff;
    --navy: #1d3f8f;
    --blue: #2a5bd0;
    --sky: #5b8ff0;
    --orange: #f26a1b;
    --ink: #3a3f4a;
    --muted: #6b717d;
  }
  * { box-sizing: border-box; margin: 0; padding: 0; }
  html, body { width: 1200px; height: 629px; overflow: hidden; }
  body {
    background: var(--backdrop);
    font-family: "Open Sans", Arial, sans-serif;
    color: var(--ink);
    position: relative;
  }
  .card {
    position: absolute;
    width: 525px;
    height: 300px;
    background: var(--card);
    box-shadow: 0 4px 14px rgba(0,0,0,.12);
    overflow: hidden;
  }
  .card--back { left: 45px; top: 165px; }
  .card--front { left: 630px; top: 165px; }

  .brand {
    font-weight: 800;
    color: var(--navy);
    font-size: 28px;
    letter-spacing: .5px;
    text-transform: uppercase;
    line-height: 1;
    display: flex;
    align-items: center;
    gap: 10px;
  }
  .brand__dot {
    width: 14px; height: 14px; border-radius: 50%;
    background: var(--orange);
    flex: none;
  }

  .card--back .brand { position: absolute; left: 70px; top: 72px; }
  .services {
    position: absolute; left: 0; right: 0; top: 150px;
    text-align: center;
    font-size: 13px;
    line-height: 1.55;
    color: var(--ink);
  }
  .services__web { color: var(--blue); font-weight: 600; margin-top: 4px; }

  .swoosh { position: absolute; inset: 0; width: 100%; height: 100%; }
  .card--front .brand { position: absolute; left: 32px; top: 142px; font-size: 24px; }
  .front-name {
    position: absolute; right: 34px; top: 150px;
    font-size: 11px; font-weight: 600; color: var(--navy);
  }
  .contact {
    position: absolute; left: 32px; top: 196px;
    list-style: none;
    font-size: 9.5px;
    line-height: 1;
    color: var(--muted);
  }
  .contact li { display: flex; align-items: center; gap: 7px; margin-bottom: 4px; }
  .contact svg { width: 9px; height: 9px; flex: none; }
</style>
</head>
<body>

<section class="card card--back" aria-label="Business card back">
  <div class="brand"><span class="brand__dot"></span>Harbor Crest Moving</div>
  <div class="services">
    <p>Local &amp; Long Distance</p>
    <p>Residential &amp; Commercial Storage Facility</p>
    <p class="services__web">www.harborcrestmoving.example</p>
  </div>
</section>

<section class="card card--front" aria-label="Business card front">
  <svg class="swoosh" viewBox="0 0 525 300" preserveAspectRatio="none" aria-hidden="true">
    <defs>
      <linearGradient id="band" x1="0" y1="0" x2="1" y2="1">
        <stop offset="0" stop-color="var(--sky)"/>
        <stop offset="1" stop-color="var(--navy)"/>
      </linearGradient>
    </defs>
    <path d="M140 0 H525 V150 C420 92 280 58 140 0 Z" fill="url(#band)"/>
    <path d="M120 0 C270 60 410 96 525 160" fill="none" stroke="var(--orange)" stroke-width="3"/>
    <path d="M0 300 H525" stroke="var(--blue)" stroke-width="6"/>
  </svg>
  <div class="brand"><span class="brand__dot"></span>Harbor Crest Moving</div>
  <p class="front-name">Harbor Crest Moving</p>
  <ul class="contact">
    <li><svg viewBox="0 0 10 10"><circle cx="5" cy="5" r="5" fill="var(--blue)"/><path d="M5 2.2a1.8 1.8 0 0 1 1.8 1.8C6.8 5.4 5 7.8 5 7.8S3.2 5.4 3.2 4A1.8 1.8 0 0 1 5 2.2z" fill="#fff"/></svg>412 West 57th Avenue</li>
    <li><svg viewBox="0 0 10 10"><circle cx="5" cy="5" r="5" fill="var(--blue)"/></svg>Brooklyn, NY 11204</li>
    <li><svg viewBox="0 0 10 10"><circle cx="5" cy="5" r="5" fill="var(--blue)"/><path d="M3 2.5l1.3 1.3-.7.8a4 4 0 0 0 1.8 1.8l.8-.7L7.5 7 6.8 7.7C4.6 7.5 2.5 5.4 2.3 3.2z" fill="#fff"/></svg>718-555-0142</li>
    <li><svg viewBox="0 0 10 10"><circle cx="5" cy="5" r="5" fill="var(--blue)"/><rect x="3" y="3" width="4" height="4" fill="#fff"/></svg>Fax 718-555-0187</li>
    <li><svg viewBox="0 0 10 10"><circle cx="5" cy="5" r="5" fill="var(--blue)"/><path d="M2.5 3.3h5v3.4h-5z M2.5 3.3L5 5.3l2.5-2" fill="none" stroke="#fff" stroke-width=".8"/></svg>Info@Harborcrestmoving.example</li>
    <li><svg viewBox="0 0 10 10"><circle cx="5" cy="5" r="5" fill="var(--blue)"/><circle cx="5" cy="5" r="2.5" fill="none" stroke="#fff" stroke-width=".8"/></svg>www.harborcrestmoving.example</li>
  </ul>
</section>

</body>
</html>
```